Flyer for customer acquisition.

Hello, We are a sportmanagement agency from Germany and we need information flyers for customer acquisition. It should be DinA4 and should have a modern but serious design. I have uploaded a information sheet, where you can find the text and the composition, the flyer should have. I also uploaded Pictures / Images, which you can use. Of course you can use other suitable images. If they are not free, I will buy them later. On the bottom of the flyer there has been the contact information. You will find them in the download section, too. If you have questions, just write me. If I forgot something, I will update the letter :) Thank you very much!
Ich brauche zusätzliche Tage um durchzusehen

```html
<!DOCTYPE html>
<html lang="de">
<head>
<meta charset="utf-8">
<title>TWK-S Flyer</title>
<link href="https://fonts.googleapis.com/css2?family=Oswald:wght@300;500;700&family=Lato:wght@400;700&display=swap" rel="stylesheet">
<style>
  :root{
    --stage:#e6e2dc;
    --paper:#f7f7f7;
    --paper-shade:#e9e9e9;
    --row-grey:#ececec;
    --ink:#111318;
    --text:#1c1c1c;
    --accent:#1a9fd6;
    --rule:#3a3d44;
  }
  *{margin:0;padding:0;box-sizing:border-box}
  html,body{width:1200px;height:1200px;overflow:hidden;background:var(--stage)}
  .flyer{
    position:absolute;left:186px;top:20px;width:894px;height:1254px;
    transform:scale(0.925);transform-origin:top left;
    background:linear-gradient(90deg,var(--paper-shade) 0%,#fafafa 50%,#ffffff 70%,var(--paper-shade) 100%);
    box-shadow:0 4px 18px rgba(0,0,0,.18);
    font-family:'Lato',sans-serif;color:var(--text);overflow:hidden;
  }
  .brand{position:absolute;left:30px;top:60px;width:320px;text-align:center}
  .brand-mark{width:46px;height:46px;border-radius:50%;background:var(--ink);margin:0 auto 14px}
  .brand-name{font-family:'Lato',sans-serif;font-weight:700;font-size:44px;letter-spacing:2px;color:var(--ink);line-height:1}
  .hero-art{position:absolute;left:575px;top:25px;width:225px;height:420px;border-radius:40px 40px 20px 20px;
    background:linear-gradient(170deg,#1c3f9e 0%,#2d7fd0 30%,#c13fc0 50%,#e9c995 75%,#a7c54a 100%);opacity:.85}
  .headline{position:absolute;left:32px;top:226px}
  .headline .company{font-family:'Oswald',sans-serif;font-weight:700;font-size:62px;color:var(--accent);line-height:1;letter-spacing:-1px}
  .headline .sub{font-family:'Oswald',sans-serif;font-weight:300;font-size:33px;color:var(--ink);line-height:1;margin-top:8px}
  .headline .main{font-family:'Oswald',sans-serif;font-weight:700;font-size:78px;color:var(--ink);line-height:1;margin-top:6px;letter-spacing:-1px}
  .headline .tagline{font-family:'Oswald',sans-serif;font-weight:500;font-size:19px;color:var(--ink);margin-top:8px}
  .grid{position:absolute;left:0;top:456px;width:894px}
  .row{position:relative;display:flex;border-top:1.5px solid var(--rule)}
  .cell{width:50%;padding:12px 26px 0 37px}
  .cell + .cell{border-left:1.5px solid var(--rule)}
  .grey{background:var(--row-grey)}
  .white{background:#fff}
  .cell.right{text-align:right;padding:10px 36px 0 12px}
  .row h2{font-family:'Lato',sans-serif;font-weight:700;font-size:22px;color:var(--accent);margin-bottom:8px;line-height:1.1}
  .row p{font-size:14px;line-height:1.3;text-align:justify}
  .cell.right p{text-align:right}
  .row p.small{font-size:12.5px}
  .band{height:22px;background:var(--row-grey);border-top:1.5px solid var(--rule)}
  .footer{position:absolute;left:0;top:1119px;width:894px;height:135px;border-top:1.5px solid var(--rule)}
  .notes{position:absolute;left:38px;top:22px;width:380px;font-size:9px;line-height:1.3}
  .notes p + p{margin-top:10px}
  .contact{position:absolute;right:38px;top:10px;text-align:right;list-style:none}
  .contact li{display:flex;align-items:center;justify-content:flex-end;gap:20px;height:30px;font-size:15px}
  .contact li.phone{font-weight:700;font-size:17px}
  .contact svg{width:16px;height:16px}
</style>
</head>
<body>
<div class="flyer">
  <div class="brand"><div class="brand-mark"></div><div class="brand-name">TWK</div></div>
  <div class="hero-art" role="img" aria-label="Farbenfrohe Silhouette eines Fußballspielers mit Ball"></div>

  <div class="headline">
    <div class="company">TWK-S</div>
    <div class="sub">NACHWUCHSFÖRDERUNG UND</div>
    <div class="main">MANGEMENT</div>
    <div class="tagline">WIR BEGLEITEN DICH AUF DEINEM WEG ZUM PROFI</div>
  </div>

  <div class="grid">
    <div class="row" style="height:103px">
      <div class="cell white"><h2>KARRIEREPLANUNG</h2><p>Wir haben deine Karriere im Blick! In enger Absprache mit deinen Eltern und dir leiten wir die richtigen Maßnahmen und Schritte ein, um dein Ziel „Profifußballer“ zu realisieren.</p></div>
      <div class="cell white"></div>
    </div>
    <div class="row" style="height:120px">
      <div class="cell grey"><h2>STÄNDIGER ANSPRECHPARTNER</h2><p>Egal um welchen Themen es sich handelt, wir sind für dich da! Ein vertrauensvolles und freundschaftliches Verhältnis ist uns besonders wichtig.</p></div>
      <div class="cell grey"></div>
    </div>
    <div class="row" style="height:87px">
      <div class="cell white"><h2>RECHTSBERATUNG/VERTRAGSRECHT</h2><p class="small">Juristendeutsch und Kleingedrucktes? Kein Problem! Wir helfen dir den Durchblick zu behalten und holen immer das Beste für dich raus.</p></div>
      <div class="cell white"></div>
    </div>
    <div class="band"></div>
    <div class="row" style="height:116px">
      <div class="cell grey"></div>
      <div class="cell right white"><h2>AUSRÜSTUNG</h2><p>Wir besorgen dir deine Ausrüstung! Unsere Beziehungen zu den großen Sportartikelherstellern ermöglichen den Abschluss von Ausrüsterverträgen*.</p></div>
    </div>
    <div class="row" style="height:100px">
      <div class="cell white"></div>
      <div class="cell right white" style="padding-right:42px"><h2>VORSORGE</h2><p>Verletzungen gehören leider zum Fußball dazu. Wir sichern dich ab, indem wir eine private Zusatzkrankenversicherung für dich abschließen.</p></div>
    </div>
    <div class="row" style="height:115px">
      <div class="cell grey"></div>
      <div class="cell right white" style="padding-left:6px"><h2>KOOPERATIONSPARTNER/NETZWERK</h2><p class="small">JOb Entscheidungsträger oder Experte, wir kennen die richtigen Leute. Zusätzlich bieten wir dir eine große Bandbreite an Leistungen, die du jederzeit in Anspruch nehmen kannst**.</p></div>
    </div>
  </div>

  <div class="footer">
    <div class="notes">
      <p>*Die Entscheidung über das Zustandekommen eines Ausrüstervertrags obliegt dem jeweiligen Sportartikelhersteller. Ist ein Abschluss aktuell nicht möglich, erhältst du von uns 2x pro Saison neue Fußballschuhe sowie weitere Ausrüstungsgegenstände.</p>
      <p>**Personal Training, Athletik-Training, Ernährungsberatung, Sportpsychologische Betreuung, uvm.</p>
    </div>
    <ul class="contact">
      <li class="phone">07121/5550123
        <svg viewBox="0 0 16 16"><circle cx="8" cy="8" r="7" fill="none" stroke="#1a9fd6" stroke-width="1.3"/><path d="M5.5 4.5l1.5 1.5-.8 1.2a5 5 0 0 0 2.6 2.6l1.2-.8 1.5 1.5-1 1c-3 0-6-3-6-6z" fill="#1a9fd6"/></svg></li>
      <li>info@twk-s.de
        <svg viewBox="0 0 16 16"><rect x="1" y="3" width="14" height="10" fill="#1a9fd6"/><path d="M1 3l7 6 7-6" fill="none" stroke="#fff" stroke-width="1.2"/></svg></li>
      <li>www.twk-s.de
        <svg viewBox="0 0 16 16" fill="none" stroke="#1a9fd6" stroke-width="1.1"><circle cx="8" cy="8" r="7"/><ellipse cx="8" cy="8" rx="3" ry="7"/><path d="M1 8h14M2.5 4.5h11M2.5 11.5h11"/></svg></li>
    </ul>
  </div>
</div>
</body>
</html>
```